Rambler Zinfandel wine label

I need a wine label designed for a new wine brand. I am open to anything, but I think the simpler and bolder the better so it will stand out on the shelf amongst the hundreds of brands out there.
Label should have the word RAMBLER buy itself with the word Zinfandel under it.

```html
<!DOCTYPE html>
<html lang="en">
<head>
<meta charset="UTF-8">
<title>Rambler Zinfandel – Wine Label</title>
<link rel="stylesheet" href="https://fonts.googleapis.com/css2?family=Lato:wght@400;700&display=swap">
<style>
  :root {
    --label-red: #ff0000;
    --label-white: #ffffff;
    --edge-shadow: rgba(120, 0, 0, 0.35);
  }
  html, body {
    margin: 0;
    padding: 0;
    overflow: hidden;
    background: var(--label-white);
  }
  .label {
    position: relative;
    width: 1200px;
    height: 720px;
    overflow: hidden;
    background: var(--label-white);
    font-family: "Lato", sans-serif;
  }
  .label__band {
    position: absolute;
    inset: 0;
    width: 1200px;
    height: 720px;
    filter: drop-shadow(0 6px 10px var(--edge-shadow));
  }
  .label__band polygon {
    fill: var(--label-red);
  }
  .label__brand {
    position: absolute;
    left: 0;
    right: 0;
    top: 325px;
    margin: 0;
    text-align: center;
    color: var(--label-red);
    font-weight: 400;
    font-size: 150px;
    line-height: 1;
    letter-spacing: 3px;
  }
  .label__varietal {
    position: absolute;
    left: 0;
    right: 0;
    top: 546px;
    margin: 0;
    text-align: center;
    color: var(--label-red);
    font-weight: 700;
    font-size: 40px;
    line-height: 1;
  }
</style>
</head>
<body>
  <main class="label">
    <svg class="label__band" viewBox="0 0 1200 720" aria-hidden="true">
      <polygon points="0,0 1200,0 1200,355 588,319 0,77"/>
    </svg>
    <h1 class="label__brand">RAMBLER</h1>
    <p class="label__varietal">Zinfandel</p>
  </main>
</body>
</html>
```